Website Design for Business Law Firm

We have a logo and now we would like a web site design for our new website. Our small firm provides creative and aggressive transactional (not litigation) legal services to advise healthcare, technology, internet-based and traditional companies and investors in such companies on healthcare, technology, financing, mergers/acquisitions, real estate and other transactions, legal compliance and general corporate and business matters.

We would like to see a website design that is professional and appropriate for executives, professionals, investors and government regulators to visit, that conveys professionalism and competence while being a little edgy and modern - no typical legal motifs such as gavels, books, or scales of justice. We advise businesses and investors and guide them through complicated issues quickly, capably and differently from other law firms. We are part of the business team and get things done.

The logo is attached, and we like gray as a color to complement it. The intention of the logo is to convey that in a storm or challenging time, people come to this firm, and people come to this firm when they need the power and disruption to change things or shake them up.

I have also enclosed a picture of our business card for consideration.

On the other hand, you can check out the current simple site at www.venhollow.example to see we have used a space motif in the past to evoke that we help create stars (the nebula featured there). This is not a necessary part of the new website and it may look better without it.

We appreciate your creativity and look forward to designs.

Industry/Entity Type

Business

Requirements
Must have
• We anticipate the following pages, and you may submit different ideas for the different pages:
• 1. Landing page
• 2. Services pages - healthcare, IT/Technology, general counsel services, financings, mergers/acquisitions, mediation/arbitration, procurement and productization
• 3. About Us including contact information
• Our name and contact information:
• Quellane Law Firm, P.C.
• 8716 SW 19th Ave.
• Portland, OR 97213
• phone: 971.555.0143
• fax: 971.555.0187
Nice to have
• Please consider designs that enhance the impressions we are looking for
Should not have
• Please no gavels, scales of justice, law books, or similar traditional legal imagery.

```html
<!DOCTYPE html>
<html lang="en">
<head>
<meta charset="utf-8">
<title>Quellane — Legal Advisory Service</title>
<link rel="stylesheet" href="https://fonts.googleapis.com/css2?family=Arimo:wght@400;700&family=Open+Sans:wght@400;600&display=swap">
<style>
  :root {
    --page: #333333;
    --header: #373737;
    --navband: #262626;
    --nav-active: #262626;
    --panel: #ffffff;
    --ink: #222222;
    --body-ink: #555555;
    --accent: #f07a2b;
    --tagline: #f2e416;
    --rule: #3a3a3a;
    --photo-a: #d9d4d0;
    --photo-b: #8a7a70;
  }
  * { box-sizing: border-box; margin: 0; padding: 0; }
  html, body { width: 1200px; height: 900px; overflow: hidden; background: var(--page); }
  body { position: relative; font-family: "Open Sans", Verdana, sans-serif; color: var(--body-ink); }

  .site-header { position: absolute; left: 0; top: 0; width: 1200px; height: 117px; background: var(--header); }
  .brand { position: absolute; left: 140px; top: 8px; }
  .brand-mark { display: flex; align-items: center; gap: 10px; height: 62px; }
  .brand-square { width: 20px; height: 20px; background: #cfd6d8; }
  .brand-name { font-family: "Arimo", Arial, sans-serif; font-size: 34px; font-weight: 400; letter-spacing: 6px; color: #e8ecee; }
  .brand-tagline { margin-top: 12px; font-family: "Arimo", Arial, sans-serif; font-size: 19px; letter-spacing: 2.2px; color: var(--tagline); }

  .contact-list { position: absolute; left: 884px; top: 14px; list-style: none; }
  .contact-list li { display: flex; align-items: center; height: 31px; font-family: "Arimo", Arial, sans-serif; font-size: 13px; color: #ffffff; }
  .contact-list svg { width: 17px; height: 17px; margin-right: 10px; }

  .nav-band { position: absolute; left: 0; top: 117px; width: 1200px; height: 59px; background: var(--navband); }
  .main-nav { position: absolute; left: 120px; top: 122px; display: flex; height: 53px; }
  .main-nav a { display: flex; align-items: center; justify-content: center; height: 53px; background: var(--panel); color: var(--ink); text-decoration: none; font-family: "Arimo", Arial, sans-serif; font-size: 13px; border-left: 1px solid var(--rule); }
  .main-nav a.is-active { background: var(--nav-active); color: #ffffff; border-left: 0; }

  .hero { position: absolute; left: 120px; top: 181px; width: 961px; height: 265px; background: var(--panel); border: 1px solid #999; }
  .hero-photo { position: absolute; bottom: 0; }
  .hero-photo--team { left: 30px; width: 280px; height: 255px; background: radial-gradient(ellipse at 50% 40%, var(--photo-a), var(--photo-b) 70%, #3a3434); border-radius: 120px 120px 0 0; }
  .hero-photo--advisor { left: 690px; width: 235px; height: 262px; background: radial-gradient(ellipse at 55% 35%, #efe2cf, #b49a7d 55%, #3b3838); border-radius: 110px 110px 0 0; }
  .hero-quote { position: absolute; left: 330px; top: 104px; width: 300px; text-align: center; font-family: "Open Sans", Verdana, sans-serif; font-size: 17px; line-height: 22px; color: var(--ink); white-space: nowrap; }

  .welcome { position: absolute; left: 120px; top: 452px; width: 960px; height: 119px; background: var(--panel); padding: 14px 15px 0 15px; }
  .welcome h1 { font-family: "Arimo", Arial, sans-serif; font-weight: 400; font-size: 20px; color: var(--ink); margin-bottom: 8px; }
  .welcome p { padding-left: 3px; font-size: 12.4px; line-height: 18px; letter-spacing: 0.45px; }

  .service-card { position: absolute; top: 578px; width: 310px; height: 284px; background: var(--panel); padding: 12px 17px 0 17px; }
  .service-card h2 { font-family: "Arimo", Arial, sans-serif; font-weight: 400; font-size: 20px; color: var(--ink); margin-bottom: 9px; }
  .service-card ul { list-style: none; }
  .service-card li { font-size: 12.4px; line-height: 18px; letter-spacing: 0.3px; }
  .read-more { position: absolute; right: 22px; bottom: 27px; color: var(--accent); font-size: 12.4px; text-decoration: none; letter-spacing: 0.3px; }
  .card-1 { left: 120px; }
  .card-2 { left: 445px; padding-left: 20px; }
  .card-3 { left: 770px; padding-left: 20px; }
  .card-3 .read-more { right: 18px; }

  .site-footer { position: absolute; left: 120px; top: 868px; width: 960px; height: 32px; background: var(--panel); display: flex; align-items: center; padding-left: 16px; }
  .copyright { font-family: "Arimo", Arial, sans-serif; font-size: 12px; color: #555; }
  .footer-nav { position: absolute; right: 18px; top: 9px; display: flex; gap: 30px; }
  .footer-nav a { font-family: "Arimo", Arial, sans-serif; font-size: 11.5px; color: var(--ink); text-decoration: none; }
</style>
</head>
<body>
  <header class="site-header">
    <div class="brand">
      <div class="brand-mark">
        <span class="brand-square"></span>
        <span class="brand-name">QUELLANE</span>
      </div>
      <div class="brand-tagline">Legal Advisory Service</div>
    </div>
    <ul class="contact-list">
      <li>
        <svg viewBox="0 0 16 16" aria-hidden="true"><circle cx="8" cy="8" r="8" fill="#f07a2b"/><path d="M5.5 4.5c-.8 2.5.8 5.8 3.6 7 .5.2 1 .1 1.3-.3l.5-.7-1.4-1.1-.7.5c-1-.6-1.6-1.5-1.9-2.5l.7-.5-.6-1.7z" fill="#fff"/></svg>
        Phone:- 971.555.0143
      </li>
      <li>
        <svg viewBox="0 0 16 16" aria-hidden="true"><circle cx="8" cy="8" r="8" fill="#f07a2b"/><rect x="5.5" y="3.8" width="5" height="3" fill="#fff"/><rect x="4" y="7" width="8" height="4" rx="0.5" fill="#fff"/><rect x="5.5" y="10" width="5" height="2.3" fill="#fff" stroke="#f07a2b" stroke-width="0.6"/></svg>
        Fax:- 971.555.0187
      </li>
      <li>
        <svg viewBox="0 0 16 16" aria-hidden="true"><circle cx="8" cy="8" r="8" fill="#f07a2b"/><rect x="4" y="5.3" width="8" height="5.6" fill="#fff"/><path d="M4 5.5l4 3 4-3" fill="none" stroke="#f07a2b" stroke-width="0.9"/></svg>
        Email:- info@venhollow.example
      </li>
    </ul>
  </header>

  <div class="nav-band"></div>
  <nav class="main-nav">
    <a class="is-active" href="#" style="width:102px">Home</a>
    <a href="#" style="width:143px">About Us</a>
    <a href="#" style="width:133px">Service</a>
    <a href="#" style="width:143px">Industries</a>
    <a href="#" style="width:139px">Careers</a>
    <a href="#" style="width:161px">Client Portal</a>
    <a href="#" style="width:139px">Contact Us</a>
  </nav>

  <section class="hero">
    <div class="hero-photo hero-photo--team" role="img" aria-label="Photo of two smiling businesswomen holding a red folder"></div>
    <p class="hero-quote">“We provide a full range of legal<br>and professional services”</p>
    <div class="hero-photo hero-photo--advisor" role="img" aria-label="Photo of a smiling businesswoman in glasses giving a thumbs up"></div>
  </section>

  <section class="welcome">
    <h1>Welcome to our site</h1>
    <p>Our small firm provides creative and aggressive transactional (not litigation) legal services to advise healthcare, technology, internet-based and traditional companies and investors in such companies on healthcare, technology, financing, mergers/acquisitions, real estate and other transactions, legal compliance and general corporate and business matters.</p>
  </section>

  <article class="service-card card-1">
    <h2>Corporate &amp; Legal Advisory</h2>
    <ul>
      <li>Strategic Alliances</li>
      <li>Business Relationships</li>
      <li>Outsourcing</li>
      <li>Procurements - Buying or Selling</li>
      <li>Licensing and Technology Exploitation</li>
      <li>Venture Formation and Startup</li>
      <li>Venture Financing</li>
      <li>Creative Private Financing Arrangements</li>
    </ul>
    <a class="read-more" href="#">Read More &gt;&gt;</a>
  </article>

  <article class="service-card card-2">
    <h2>Business Mentoring</h2>
    <ul>
      <li>Mergers and Acquisitions</li>
      <li>Real Estate</li>
      <li>Contracts</li>
      <li>Audits, Analyses and Legal Project Management</li>
      <li>Local Counsel for Transactions and Due Diligence</li>
      <li>Vendor Management</li>
      <li>Dispute Resolution</li>
      <li>Service as a Mediator or Arbitrator</li>
    </ul>
    <a class="read-more" href="#">Read More &gt;&gt;</a>
  </article>

  <article class="service-card card-3">
    <h2>Mgmt. &amp; Tech. Solutions</h2>
    <ul>
      <li>Mergers and Acquisitions</li>
      <li>Real Estate</li>
      <li>Contracts</li>
      <li>Audits, Analyses and Legal Project Management</li>
      <li>Local Counsel for Transactions and Due Diligence</li>
      <li>Vendor Management</li>
      <li>Dispute Resolution</li>
      <li>Service as a Mediator or Arbitrator</li>
    </ul>
    <a class="read-more" href="#">Read More &gt;&gt;</a>
  </article>

  <footer class="site-footer">
    <span class="copyright">© Copyright 2013 venhollow.example, All Rights Reserved.</span>
    <nav class="footer-nav">
      <a href="#">Home</a>
      <a href="#">About Us</a>
      <a href="#">Service</a>
      <a href="#">Industries</a>
      <a href="#">Careers</a>
      <a href="#">Client Portal</a>
      <a href="#">Contact Us</a>
    </nav>
  </footer>
</body>
</html>
```